Uplift: Covid 19 (Poster)

We are looking to create a 11 by 17 inch 1 page poster.
-- Please Include NKR’s logo
-- Use the colors and font and mimic the feel of from Steady Step, Steady Breath Resource - Dementia Risk Reduction Flyers - Northern Council for Tribal Longevity (nkrcircle.org)
--> https://nkrcircle.org/resource-dementia-risk-reduction-flyers/
Moto needs to be included and it is: Protect Your Community. Protect Your Elders. Stay Vaccinated.
Include funding statement at the bottom of document - small print:
This project is supported by the Bureau for Illness Monitoring and Response of the U.S. Office of Wellness and Family Programs (OWFP) as part of a financial assistance award totaling $20,007,444 with 100 percent funded by BIMR/OWFP. The contents are those of the author(s) and do not necessarily represent the official views of, nor an endorsement, by BIMR/OWFP, or the U.S. Government.

```html
<!DOCTYPE html>
<html lang="en">
<head>
<meta charset="utf-8">
<title>Fight COVID-19! – Northern Council for Tribal Longevity</title>
<link href="https://fonts.googleapis.com/css2?family=Carlito:wght@400;700&family=Noto+Sans:wght@400;700;800&display=swap" rel="stylesheet">
<style>
  :root {
    --page-grey: #7f7f7f;
    --cream: #f3ebdd;
    --teal: #23757a;
    --teal-dark: #1b5f63;
    --red: #e0173a;
    --brick: #b8503f;
    --brown: #7b3a12;
    --ink: #111111;
    --white: #ffffff;
    --border-grey: #6d6d6d;
  }
  * { box-sizing: border-box; margin: 0; padding: 0; }
  html, body {
    width: 858px; height: 1200px; overflow: hidden;
    background: var(--page-grey);
  }
  .poster {
    position: absolute; left: 84px; top: 67px;
    width: 690px; height: 1065px;
    background: var(--cream);
    overflow: hidden;
    font-family: "Carlito", "Calibri", sans-serif;
    color: var(--ink);
  }
  .corner-wave { position: absolute; left: 0; top: 0; width: 690px; height: 300px; }

  .brand {
    position: absolute; left: 352px; top: 46px; width: 317px; height: 70px;
    background: var(--white);
    border-radius: 35px 0 0 35px;
    display: flex; align-items: center; gap: 12px;
    padding-left: 26px;
  }
  .brand-mark { width: 14px; height: 14px; background: var(--teal); flex: none; }
  .brand-name {
    font-family: "Carlito", sans-serif; font-weight: 700;
    font-size: 19px; line-height: 1.05; color: var(--brick);
    text-transform: uppercase; letter-spacing: 0.3px;
  }

  .headline { position: absolute; left: 41px; color: var(--red); font-weight: 700; line-height: 1; }
  .headline-fight { top: 44px; font-size: 135px; letter-spacing: -1px; }
  .headline-covid { top: 182px; font-size: 62px; }

  .art { position: absolute; }
  .art-kick {
    left: 331px; top: 150px; width: 148px; height: 124px;
    background: radial-gradient(circle at 30% 55%, #d8243c 0 26%, transparent 27%),
                linear-gradient(120deg, rgba(35,117,122,0.0) 40%, rgba(53,170,170,0.55) 60%, rgba(53,170,170,0.0) 90%);
    border-radius: 12px;
  }
  .art-elders {
    left: 423px; top: 165px; width: 267px; height: 410px;
    background: linear-gradient(180deg, rgba(243,235,221,0) 0%, #b86aa9 18%, #8a2a7a 45%, #c2452d 70%, #e88d3a 100%);
    border-radius: 70px 0 0 0;
  }

  .intro {
    position: absolute; left: 45px; top: 251px; width: 440px;
    font-size: 20px; line-height: 29px;
  }
  .intro-lead { font-weight: 700; }
  .intro-point { font-weight: 400; }

  .symptom-band {
    position: absolute; left: 0; top: 575px; width: 690px; height: 59px;
    background: var(--teal);
    border-top: 4px solid var(--brown);
    border-bottom: 4px solid var(--brown);
    padding: 4px 71px 0 45px;
    font-family: "Noto Sans", sans-serif; font-weight: 800;
    font-size: 17px; line-height: 23.5px; color: var(--white);
    letter-spacing: 0.4px;
    text-align: justify; text-align-last: justify;
    text-shadow: 1px 1px 0 #0d3335, -1px -1px 0 #0d3335, 1px -1px 0 #0d3335, -1px 1px 0 #0d3335;
  }

  .symptoms { position: absolute; left: 0; top: 645px; list-style: none; }
  .symptom {
    height: 22px; margin-bottom: 6.5px;
    background: var(--teal); color: var(--white);
    font-size: 19px; line-height: 22px;
    padding-left: 39px; white-space: nowrap;
    display: flex; gap: 16px;
  }
  .symptom span::before { content: "\25C6"; font-size: 12px; margin-right: 3px; position: relative; top: -2px; }

  .art-doctor {
    left: 436px; top: 641px; width: 235px; height: 400px;
    background: linear-gradient(180deg, #eceae6 0%, #f7f6f3 60%, #e6e3de 100%);
    border-radius: 60px 60px 0 0;
  }
  .motto-shield { position: absolute; left: 436px; top: 688px; width: 140px; height: 165px; }
  .motto {
    position: absolute; left: 452px; top: 722px; width: 110px;
    transform: rotate(-8deg);
    text-align: center; font-family: "Noto Sans", sans-serif; font-weight: 700;
    font-size: 8.6px; line-height: 13px; text-transform: uppercase; color: var(--ink);
  }
  .motto-stay { display: block; font-size: 19px; line-height: 17px; font-weight: 800; }
  .motto-vacc { display: block; font-size: 9px; line-height: 10px; }

  .funding {
    position: absolute; left: 42px; top: 926px; width: 574px; height: 97px;
    background: var(--white);
    border: 2px solid var(--border-grey);
    border-radius: 20px;
    padding: 8px 26px 0 27px;
    font-family: "Noto Sans", sans-serif; font-size: 11.3px; line-height: 15.3px;
    text-align: justify; text-align-last: justify; letter-spacing: 0.2px;
  }
  .funding p { text-align-last: justify; }

  .border-pattern {
    position: absolute; left: 0; top: 1039px; width: 690px; height: 26px;
    background: linear-gradient(90deg, #8c1f2d 0%, #b34a3a 45%, #23757a 100%);
  }
</style>
</head>
<body>
<main class="poster">
  <svg class="corner-wave" viewBox="0 0 690 300" aria-hidden="true">
    <path d="M349 0 C392 0 404 40 424 72 C452 118 486 150 560 150 C640 150 672 172 690 205 L690 0 Z" fill="var(--teal)"/>
  </svg>

  <div class="brand">
    <span class="brand-mark"></span>
    <span class="brand-name">Northern Council for<br>Tribal Longevity</span>
  </div>

  <h1 class="headline headline-fight">Fight</h1>
  <h2 class="headline headline-covid">COVID-19!</h2>

  <div class="art art-kick" role="img" aria-label="Illustration of a masked woman kicking a red coronavirus particle"></div>
  <div class="art art-elders" role="img" aria-label="Photograph of two Native elder women in traditional velvet clothing and a patterned blanket"></div>

  <div class="intro">
    <p class="intro-lead">American Indian and Alaska Native people<br>have a higher risk of COVID-19 infection rate<br>than other population in the United States.</p>
    <p class="intro-point">•COVID-19 is a virus that spreads<br>mainly when infected people<br>cough, sneeze, or talk.</p>
    <p class="intro-point">•The best way to prevent yourself<br>and others from COVID-19 is by<br>staying up to date with vaccination<br>boosters.</p>
  </div>

  <div class="symptom-band">COVID-19 symptoms may take 2 to 14 days to appear after exposure to the virus, and symptoms may include:</div>

  <div class="art art-doctor" role="img" aria-label="Illustration of a masked doctor in a white coat raising a fist and holding a shield"></div>

  <ul class="symptoms">
    <li class="symptom" style="width:561px"><span>Fever or chills</span></li>
    <li class="symptom" style="width:550px"><span>Cough</span></li>
    <li class="symptom" style="width:465px"><span>Shortness of breath or difficulty breathing</span></li>
    <li class="symptom" style="width:444px"><span>Fatigue</span><span>Muscle or body aches</span></li>
    <li class="symptom" style="width:450px"><span>Headache</span></li>
    <li class="symptom" style="width:460px"><span>New loss of taste or smell</span></li>
    <li class="symptom" style="width:471px"><span>Sore throat</span></li>
    <li class="symptom" style="width:513px"><span>Congestion or runny nose</span></li>
    <li class="symptom" style="width:513px"><span>Nausea or vomiting</span><span style="margin-left:6px">Diarrhea</span></li>
  </ul>

  <svg class="motto-shield" viewBox="0 0 140 165" aria-hidden="true">
    <path d="M8 30 Q70 -4 124 14 L132 112 Q118 148 70 162 Q30 146 18 116 Z" fill="var(--teal-dark)"/>
    <path d="M18 36 Q70 8 116 22 L122 108 Q110 138 70 150 Q36 136 27 110 Z" fill="var(--white)"/>
  </svg>
  <p class="motto">Protect your<br>community.<br>Protect your<br>elders.<span class="motto-stay">Stay</span><span class="motto-vacc">vaccinated.</span></p>

  <div class="funding">
    <p>This project is supported by the Bureau for Illness Monitoring and Response of the U.S. Office of Wellness and Family Programs (OWFP) as part of a financial assistance award totaling $20,007,444 with 100 percent funded by BIMR/OWFP. The contents are those of the author(s) and do not necessarily represent the official views of, nor an endorsement, by BIMR/OWFP, or the U.S. Government.</p>
  </div>

  <div class="border-pattern" role="img" aria-label="Decorative zigzag border pattern in red and teal"></div>
</main>
</body>
</html>
```